Fire Risk Assessment App needs a sleek UI design

I need a sleek, modern but professional design for my 5 page Fire Risk Assessment App. Include gradient background, fire themed colours including reds, yellows, light orange and a touch of black. Design must ooze simplicity and professionalism. This is for the UK market. See attached images and word doc for more information.

Target Market(s)

General public and business owners

Industry/Entity Type

Technology / Fire Safety

Colors
00AB8E
00BBA5
67D7C9
C6EFE9
E9F9F6
59FF00
82FF00
B8FF75
E3FFCB
F4FFEA
FFC000
F8CF3A
FAE287
FDF2CF
FEFAEE
F0912C
F2A743
F7CA91
FBE8D2
FDF5EE
EE7325
F08F49
F5BC92
FAE3D3
FDF4ED
EB3D1F
EC4F4E
F09395
F8D3D4
FCEDEE

```html
<!DOCTYPE html>
<html lang="en">
<head>
<meta charset="utf-8">
<title>Fire Risk Assessment App</title>
<link rel="stylesheet" href="https://fonts.googleapis.com/css2?family=Rubik:wght@400;500;600;700&display=swap">
<style>
:root{
  --ink:#2b2b2b;
  --white:#ffffff;
  --cream:#fdf2cf;
  --cream-soft:#fef6dc;
  --yellow:#ffc000;
  --yellow-2:#f8cf3a;
  --yellow-pale:#fae287;
  --orange:#f0912c;
  --orange-deep:#ee7325;
  --orange-soft:#f08f49;
  --red:#eb3d1f;
  --red-2:#ec4f4e;
  --red-pale:#f8d3d4;
  --green:#00ab00;
  --green-bright:#b8ff75;
  --teal:#00bba5;
  --teal-pale:#c6efe9;
}
*{margin:0;padding:0;box-sizing:border-box}
html,body{width:1005px;height:1200px;overflow:hidden;background:var(--white)}
body{position:relative;font-family:"Rubik",sans-serif;color:var(--ink)}
.page-title{position:absolute;left:0;width:1005px;top:90px;text-align:center;font-size:46px;font-weight:600;letter-spacing:-0.5px}
.side-label{position:absolute;font-size:21px;font-weight:500;letter-spacing:9px;white-space:nowrap;transform:translate(-50%,-50%) rotate(-90deg)}
.side-label.landing{left:94px;top:597px}
.side-label.dashboard{left:906px;top:725px}
.closing-note{position:absolute;left:113px;top:1045px;font-size:21px;font-weight:500;letter-spacing:.3px}

.screen{position:absolute;width:297px;border-radius:16px;overflow:hidden;background:var(--cream);box-shadow:0 0 0 1px #eee}
.screen.landing{left:151px;top:221px;height:714px}
.screen.dashboard{left:557px;top:330px;height:791px}
.abs{position:absolute}
.status{position:absolute;left:0;top:6px;width:100%;height:16px;color:var(--white);font-size:9.5px;font-weight:600;padding:0 13px;display:flex;justify-content:space-between;align-items:center;z-index:3}
.status svg{display:block}

/* landing */
.hero{position:absolute;left:0;top:0;width:297px;height:371px;border-radius:0 0 16px 16px;background:linear-gradient(180deg,var(--yellow) 0%,#f9a91c 40%,var(--orange-deep) 100%)}
.hero-line{position:absolute;width:100%;text-align:center;color:var(--white);font-size:14px}
.hero-line.one{top:46px}
.hero-line.two{top:71px;font-weight:700}
.ghost-card{position:absolute;width:110px;height:180px;border-radius:10px;background:rgba(255,240,210,.35)}
.ghost-card.left{left:38px;top:138px;transform:rotate(-8deg)}
.ghost-card.right{left:150px;top:140px;transform:rotate(8deg)}
.q-card{position:absolute;left:76px;top:117px;width:151px;height:225px;border-radius:9px;background:var(--white);overflow:hidden;box-shadow:0 4px 12px rgba(160,60,0,.25)}
.q-head{height:36px;background:linear-gradient(90deg,var(--orange-deep),var(--orange));color:var(--white);font-size:7px;font-weight:700;padding:8px 0 0 10px;line-height:1.5}
.q-edit{position:absolute;right:6px;top:8px;width:19px;height:19px;border-radius:50%;background:var(--white)}
.q-section{background:#f7f7f7;height:44px;padding:8px 10px;font-size:6px;line-height:1.9}
.q-bolt{position:absolute;left:64px;top:72px;width:20px;height:20px;border-radius:50%;background:var(--white)}
.q-text{position:absolute;left:10px;top:95px;width:135px;font-size:6px;line-height:1.75}
.q-actions{position:absolute;left:10px;top:137px;display:flex;gap:13px}
.q-actions span{width:12px;height:12px;border-radius:50%;display:block}
.q-input{position:absolute;left:10px;top:158px;width:131px;height:15px;border:1px solid #ddd;border-radius:3px;font-size:5.5px;color:#777;padding:4px 7px}
.q-photo{position:absolute;top:183px;width:61px;height:33px;border-radius:2px;background:linear-gradient(180deg,#4a3326,#e0531b 60%,#7a2c14)}
.voice-band{position:absolute;left:0;top:371px;width:297px;height:74px;background:#fde9a6}
.mic-badge{position:absolute;left:23px;top:385px;width:50px;height:50px;border-radius:50%;background:linear-gradient(180deg,var(--yellow),var(--orange-deep));display:flex;align-items:center;justify-content:center}
.voice-text{position:absolute;left:94px;top:391px;font-size:12px;line-height:21px;color:#3a3a3a}
.pill{position:absolute;left:17px;width:262px;height:52px;border-radius:26px;color:var(--white);font-size:16px;display:flex;align-items:center;padding-left:63px}
.pill .icon{position:absolute;left:8px;top:7px;width:38px;height:38px;border-radius:50%;background:var(--white);display:flex;align-items:center;justify-content:center}
.pill.create{top:473px;background:linear-gradient(90deg,var(--orange),var(--yellow-2) 55%,var(--orange))}
.pill.login{top:574px;background:linear-gradient(90deg,var(--red),var(--red-2) 55%,var(--red))}
.note{position:absolute;width:100%;text-align:center;font-size:11px;color:#333}
.note .accent{color:var(--red)}

/* dashboard */
.dash-head{position:absolute;left:0;top:0}
.dash-title{position:absolute;left:125px;top:41px;color:var(--white);font-size:17px;font-weight:700}
.dash-gauge{position:absolute;left:83px;top:40px}
.start-label{position:absolute;top:90px;width:100%;text-align:center;color:var(--white);font-size:13.5px}
.plus-btn{position:absolute;left:110px;top:130px;width:78px;height:78px;border-radius:50%;background:var(--white);display:flex;align-items:center;justify-content:center}
.type-badge{position:absolute;top:189px;width:78px;height:78px;border-radius:50%;background:var(--white);display:flex;align-items:center;justify-content:center}
.type-badge.commercial{left:10px}
.type-badge.residential{left:211px}
.type-badge .art{width:46px;height:46px;border-radius:8px}
.type-label{position:absolute;top:275px;font-size:9px;font-weight:500;width:90px;text-align:center}
.type-label.commercial{left:4px}
.type-label.residential{left:205px}
.group{position:absolute;left:12px;width:272px;border-radius:14px}
.group.complete{top:315px;height:100px;background:var(--green-bright)}
.group.progress{top:426px;height:157px;background:var(--teal-pale)}
.group.purchases{top:604px;height:153px;background:var(--red-pale)}
.group-head{position:absolute;left:18px;top:10px;display:flex;align-items:center;gap:9px;font-size:10px;font-weight:500}
.group-head .dot{width:16px;height:16px;border-radius:50%;display:flex;align-items:center;justify-content:center}
.group-list{position:absolute;left:6px;width:260px;background:var(--white);border-radius:12px}
.complete .group-list{top:38px;height:56px}
.progress .group-list{top:43px;height:107px}
.purchases .group-list{top:42px;height:107px}
.row{position:absolute;left:0;width:100%;height:40px;display:flex;align-items:center;font-size:12px;color:#333}
.row .thumb{position:absolute;left:9px;width:38px;height:38px;border-radius:50%;background:var(--cream)}
.row .thumb::after{content:"";position:absolute;left:11px;top:9px;width:16px;height:20px;border-radius:3px;background:linear-gradient(180deg,#e6a15a,#7aa6d9)}
.row .name{position:absolute;left:56px}
</style>
</head>
<body>

<h1 class="page-title">Fire Risk Assessment App</h1>
<div class="side-label landing">01.LANDING PAGE</div>
<div class="side-label dashboard">02.DASHBOARD</div>
<p class="closing-note">THANKS FOR WATCHING MY WORKS</p>

<!-- Landing screen -->
<section class="screen landing">
  <div class="hero" role="img" aria-label="Orange flame backdrop"></div>
  <div class="status"><span>5:50 am</span>
    <svg width="44" height="10" viewBox="0 0 44 10" fill="#fff"><path d="M2 4a7 7 0 0 1 10 0l-1 1a5.5 5.5 0 0 0-8 0zM4.5 6a3.5 3.5 0 0 1 5 0L7 8.5z"/><rect x="21" y="6" width="2" height="4"/><rect x="24" y="3" width="2" height="7"/><rect x="27" y="0" width="2" height="10"/><rect x="34" y="1.5" width="9" height="7" rx="1.5" fill="none" stroke="#fff"/><rect x="35.5" y="3" width="6" height="4"/></svg>
  </div>
  <p class="hero-line one">The Most "User Friendly"</p>
  <p class="hero-line two">Fire Risk Assessment App Available</p>
  <div class="ghost-card left"></div>
  <div class="ghost-card right"></div>
  <div class="q-card">
    <div class="q-head">FIRE RISK ASSESSMENT<br>FIRE HAZARDS</div>
    <span class="q-edit"></span>
    <div class="q-section">SECTION 7-00/30.00<br>Electronic Sources of Ignition</div>
    <div class="q-bolt">
      <svg width="20" height="20" viewBox="0 0 20 20"><circle cx="10" cy="10" r="7" fill="#ffc000"/><path d="M11 4 6.5 11H10l-1 5 4.5-7H10z" fill="#2b2b2b"/></svg>
    </div>
    <div class="q-text"><strong style="font-weight:500">Q:7:01</strong><br>Are reasonable measures taken do prevent fires of electrical origin?</div>
    <div class="q-actions">
      <span style="background:#00ab00"></span><span style="background:#eb3d1f"></span><span style="background:#ffc000"></span><span style="background:#00bba5"></span><span style="background:#ee7325"></span>
    </div>
    <div class="q-input">No, electric sockets are overloaded</div>
    <div class="q-photo" style="left:10px" role="img" aria-label="Photo of a house on fire"></div>
    <div class="q-photo" style="left:80px" role="img" aria-label="Photo of a burning building at night"></div>
  </div>

  <div class="voice-band"></div>
  <div class="mic-badge">
    <svg width="22" height="28" viewBox="0 0 22 28" fill="none" stroke="#fff" stroke-width="2.2" stroke-linecap="round"><rect x="7" y="2" width="8" height="14" rx="4"/><path d="M3 12a8 8 0 0 0 16 0M11 20v5M6 25h10"/></svg>
  </div>
  <p class="voice-text">Quick tap response and voice<br>activated typing</p>

  <div class="pill create">
    <span class="icon"><svg width="22" height="22" viewBox="0 0 22 22"><circle cx="9" cy="6" r="4" fill="#f8a31c"/><path d="M1 19a8 7 0 0 1 14 0z" fill="#f8a31c"/><circle cx="17" cy="16" r="4.5" fill="#f08f49"/><path d="M17 13.5v5M14.5 16h5" stroke="#fff" stroke-width="1.4"/></svg></span>
    Create a Free Account
  </div>
  <p class="note" style="top:542px">Any Responsible Person can do it</p>
  <div class="pill login">
    <span class="icon"><svg width="22" height="22" viewBox="0 0 22 22"><circle cx="9" cy="6" r="4" fill="#eb3d1f"/><path d="M1 19a8 7 0 0 1 14 0z" fill="#eb3d1f"/><circle cx="17" cy="16" r="4.5" fill="#ec4f4e"/><rect x="15" y="15.5" width="4" height="3" fill="#fff"/><path d="M15.8 15.5v-1a1.2 1.2 0 0 1 2.4 0v1" stroke="#fff" fill="none"/></svg></span>
    Customer Login
  </div>
  <p class="note" style="top:641px">Created and endorsed by</p>
  <p class="note" style="top:660px">British Firefighters <span class="accent">(it is true)</span></p>
</section>

<!-- Dashboard screen -->
<section class="screen dashboard">
  <svg class="dash-head" width="297" height="226" viewBox="0 0 297 226" role="img" aria-label="Orange flame header">
    <defs><linearGradient id="headFill" x1="0" y1="0" x2="0" y2="1"><stop offset="0" stop-color="#f9ae1a"/><stop offset="1" stop-color="#ee7325"/></linearGradient></defs>
    <path d="M0 0H297V160Q297 176 281 176H214Q198 176 191 192Q178 225 149 225Q120 225 107 192Q100 176 84 176H16Q0 176 0 160Z" fill="url(#headFill)"/>
  </svg>
  <div class="status"><span>5:50 am</span>
    <svg width="44" height="10" viewBox="0 0 44 10" fill="#fff"><path d="M2 4a7 7 0 0 1 10 0l-1 1a5.5 5.5 0 0 0-8 0zM4.5 6a3.5 3.5 0 0 1 5 0L7 8.5z"/><rect x="21" y="6" width="2" height="4"/><rect x="24" y="3" width="2" height="7"/><rect x="27" y="0" width="2" height="10"/><rect x="34" y="1.5" width="9" height="7" rx="1.5" fill="none" stroke="#fff"/><rect x="35.5" y="3" width="6" height="4"/></svg>
  </div>
  <svg class="dash-gauge" width="30" height="22" viewBox="0 0 30 22" fill="none" stroke="#fff" stroke-width="3" stroke-linecap="round"><path d="M3 19A12 12 0 1 1 27 19Z" fill="#fff" stroke="none"/><path d="M7 17A8 8 0 1 1 23 17" stroke="#f5a01e" stroke-width="2"/><path d="M15 16l5-6" stroke="#f5a01e" stroke-width="2"/></svg>
  <div class="dash-title">Dashboard</div>
  <p class="start-label">START FIRE RISK ASSESSMENT</p>
  <div class="plus-btn">
    <svg width="38" height="38" viewBox="0 0 38 38"><path d="M19 4v30M4 19h30" stroke="#ee7325" stroke-width="5.5" stroke-linecap="round"/></svg>
  </div>
  <div class="type-badge commercial"><span class="art" role="img" aria-label="Illustration of a commercial office building" style="background:linear-gradient(180deg,#e85b3c,#5f8fd6 45%,#5cbf4a)"></span></div>
  <div class="type-badge residential"><span class="art" role="img" aria-label="Illustration of a residential house" style="background:linear-gradient(180deg,#6d7580,#eef0f2 45%,#d96a5a)"></span></div>
  <p class="type-label commercial">COMMERCIAL</p>
  <p class="type-label residential">RESIDENTIAL</p>

  <div class="group complete">
    <div class="group-head"><span class="dot" style="background:#00ab00"><svg width="8" height="8" viewBox="0 0 8 8"><path d="M1 4l2 2 4-4" stroke="#fff" stroke-width="1.5" fill="none"/></svg></span>COMPLETE</div>
    <div class="group-list">
      <div class="row" style="top:8px"><span class="thumb" role="img" aria-label="Building icon"></span><span class="name">Reggie's Barbershop</span></div>
    </div>
  </div>

  <div class="group progress">
    <div class="group-head"><span class="dot" style="background:#00bba5;width:20px;height:20px"><svg width="12" height="12" viewBox="0 0 12 12" fill="none" stroke="#fff" stroke-width="1.6"><path d="M10 6a4 4 0 1 1-1.2-2.9"/><path d="M9.5 1v2.5H7"/></svg></span>IN PROGRESS</div>
    <div class="group-list">
      <div class="row" style="top:12px"><span class="thumb" role="img" aria-label="Building icon"></span><span class="name">Elm Road School</span></div>
      <div class="row" style="top:59px"><span class="thumb" role="img" aria-label="House icon"></span><span class="name">St Anne's Care Home</span></div>
    </div>
  </div>

  <div class="group purchases">
    <div class="group-head"><span class="dot" style="background:#f09395;width:20px;height:20px"><svg width="10" height="11" viewBox="0 0 10 11" fill="none" stroke="#fff" stroke-width="1.2"><rect x="1" y="3.5" width="8" height="6.5" rx="1"/><path d="M3 3.5V3a2 2 0 0 1 4 0v.5"/></svg></span>PURCHASES</div>
    <div class="group-list">
      <div class="row" style="top:10px"><span class="thumb" role="img" aria-label="Building icon"></span><span class="name">Residential Fire Risk Assessment</span></div>
      <div class="row" style="top:56px"><span class="thumb" role="img" aria-label="House icon"></span><span class="name">Commercial Fire Risk Assessment</span></div>
    </div>
  </div>
</section>

</body>
</html>
```